Seafood company needs a label design

Our brand name is Coral Tide Fisheries. We need a label design for a new product line of 200g trays of sardine fillets. The label/sleeve is going to wrap around the black tray. We are a family owned and operated business in Esperance, Western Australia. We would like simple appealing designs that catch the eye of the consumer.

Target Market(s)

seafood consumers in supermarkets

Colors

Designer to choose colors to be used in the design.

Requirements
Must have
• The front of the label must include
• •Coral Tide Fisheries
• •since 1997
• •Sustainably wild caught from the pristine southern ocean Esperance Western Australia
Nice to have
• Deep/Rich colours, and black, maybe Drawn picture of sardine/sardines or an anchor fast anchor.
Should not have
• cartoon images, not too cluttered

```html
<!DOCTYPE html>
<html lang="en">
<head>
<meta charset="utf-8">
<title>Coral Tide Fisheries – Sardine Fillets Label</title>
<link rel="stylesheet" href="https://fonts.googleapis.com/css2?family=Gemunu+Libre:wght@600&family=Kaushan+Script&family=Kalam:wght@400;700&family=Playfair+Display:ital@1&display=swap">
<style>
  :root {
    --label-black: #000000;
    --gold: #d4af0a;
    --gold-deep: #a98306;
    --white: #ffffff;
    --navy: #2a416f;
    --navy-deep: #22365f;
    --sea-light: #4aa9cf;
    --sea-mid: #1fa9cf;
    --sea-bright: #18c0dc;
    --fish-silver: #8d9aa4;
  }
  html, body {
    margin: 0;
    padding: 0;
    overflow: hidden;
    background: var(--label-black);
  }
  .label {
    position: relative;
    width: 1200px;
    height: 666px;
    overflow: hidden;
    background: var(--label-black);
  }
  .label-art {
    position: absolute;
    inset: 0;
    display: block;
  }
  .product-title {
    font-family: "Gemunu Libre", "Arial Narrow", sans-serif;
    font-weight: 600;
    font-size: 196px;
    letter-spacing: 4px;
  }
  .product-variant {
    font-family: "Playfair Display", "Times New Roman", serif;
    font-style: italic;
    font-size: 92px;
    fill: var(--white);
  }
  .brand-name {
    font-family: "Kaushan Script", cursive;
    font-size: 44px;
    fill: var(--white);
  }
  .brand-since {
    font-family: "Kalam", cursive;
    font-size: 34px;
    letter-spacing: 2px;
    fill: var(--white);
  }
  .origin-claim {
    font-family: "Kalam", cursive;
    font-weight: 700;
    font-size: 44px;
    letter-spacing: 1.5px;
    fill: var(--white);
  }
  .net-weight {
    font-family: "Kalam", cursive;
    font-weight: 700;
    font-size: 32px;
    letter-spacing: 2px;
    fill: var(--white);
  }
</style>
</head>
<body>
<div class="label">
  <svg class="label-art" viewBox="0 0 1200 666" width="1200" height="666" xmlns="http://www.w3.org/2000/svg">
    <defs>
      <linearGradient id="sea-fill" x1="0" y1="0" x2="0.4" y2="1">
        <stop offset="0" stop-color="var(--sea-light)"/>
        <stop offset="0.55" stop-color="var(--sea-mid)"/>
        <stop offset="1" stop-color="var(--sea-bright)"/>
      </linearGradient>
      <radialGradient id="fish-tone" cx="0.55" cy="0.85" r="0.35">
        <stop offset="0" stop-color="var(--fish-silver)" stop-opacity="0.7"/>
        <stop offset="1" stop-color="var(--fish-silver)" stop-opacity="0"/>
      </radialGradient>
      <linearGradient id="title-gold" x1="0" y1="0" x2="0" y2="1">
        <stop offset="0" stop-color="var(--gold)"/>
        <stop offset="1" stop-color="var(--gold-deep)"/>
      </linearGradient>
      <linearGradient id="reflection-fade" x1="0" y1="0" x2="0" y2="1">
        <stop offset="0" stop-color="var(--gold)" stop-opacity="0.35"/>
        <stop offset="1" stop-color="var(--gold)" stop-opacity="0"/>
      </linearGradient>
      <linearGradient id="panel-navy" x1="0" y1="0" x2="0" y2="1">
        <stop offset="0" stop-color="var(--navy)"/>
        <stop offset="1" stop-color="var(--navy-deep)"/>
      </linearGradient>
      <filter id="soft-shadow" x="-10%" y="-10%" width="120%" height="130%">
        <feDropShadow dx="3" dy="4" stdDeviation="3" flood-color="#000" flood-opacity="0.6"/>
      </filter>
    </defs>

    <!-- sea photo panel with gold edge and white pinstripe -->
    <path class="sea-panel-edge" d="M0 0 H790 C758 272 532 542 0 586 Z" fill="var(--gold)"/>
    <g role="img" aria-label="Photograph of blue ocean water with two whole silver sardines rising from the lower edge">
      <path class="sea-panel" d="M0 0 H772 C740 262 520 526 0 570 Z" fill="url(#sea-fill)"/>
      <path d="M0 0 H772 C740 262 520 526 0 570 Z" fill="url(#fish-tone)"/>
    </g>
    <path class="sea-panel-pinstripe" d="M799 0 C766 282 540 560 0 601" fill="none" stroke="var(--white)" stroke-width="5"/>

    <!-- origin panel -->
    <path class="origin-panel-edge" d="M1200 324 C892 316 606 448 508 666 H1200 Z" fill="var(--gold)"/>
    <path class="origin-panel-pinstripe" d="M1200 336 C900 330 622 458 526 666 H1200 Z" fill="var(--white)"/>
    <path class="origin-panel" d="M1200 344 C906 338 632 466 540 666 H1200 Z" fill="url(#panel-navy)"/>

    <!-- product title -->
    <text class="product-title" x="100" y="212" transform="scale(1,-0.45) translate(0,-700)" fill="url(#reflection-fade)">Sardines</text>
    <text class="product-title" x="100" y="185" fill="url(#title-gold)" filter="url(#soft-shadow)">Sardines</text>
    <text class="product-variant" transform="translate(322 372) rotate(-40)" filter="url(#soft-shadow)">fillets</text>

    <!-- brand -->
    <text class="brand-name" x="1177" y="86" text-anchor="end">Coral Tide Fisheries</text>
    <text class="brand-since" x="1163" y="140" text-anchor="end">since 1997</text>

    <!-- origin claim -->
    <g class="origin-claim" text-anchor="end" filter="url(#soft-shadow)">
      <text x="1178" y="440">Sustainably</text>
      <text x="1178" y="503">wild caught from the</text>
      <text x="1178" y="566">pristine Southern Ocean</text>
      <text x="1178" y="629">Esperance Western Australia</text>
    </g>

    <!-- net weight -->
    <text class="net-weight" x="42" y="648">200g</text>
  </svg>
</div>
</body>
</html>
```